Uplift: Covid 19 Fact Sheet (2 page)

We are looking to create a 2-page Fact Sheet (front and back)
-- Please Include NC4’s logo
-- Use the colors and font and mimic the feel of from Strong Spirit, Steady Mind Resource - Dementia Risk Reduction Flyers - Northern Circle for Elder Wellness (ncfour.org)
--> https://ncfour.org/resource-dementia-risk-reduction-flyers/
Moto needs to be included and it is: Protect Your Community. Protect Your Elders. Stay Vaccinated.
Include funding statement at bottom of document - small print:
This project is supported by the Bureau for Public Wellness Oversight of the Federal Office of Civic Care and Welfare (OCW) as part of a financial assistance award totaling $20,007,444 with 100 percent funded by BPW/OCW. The contents are those of the author(s) and do not necessarily represent the official views of, nor an endorsement, by BPW/OCW, or the U.S. Government.

```html
<!DOCTYPE html>
<html lang="en">
<head>
<meta charset="utf-8">
<title>Uplift – COVID-19 Fact Sheet, Front and Back</title>
<link rel="stylesheet" href="https://fonts.googleapis.com/css2?family=Baloo+2:wght@600;700;800&family=Mulish:ital,wght@0,400;0,700;0,800;1,400;1,700&display=swap">
<style>
:root{
  --backdrop:#ebe5dc;
  --paper:#f3eadb;
  --brown:#6e2c14;
  --teal:#2b8796;
  --teal-soft:#4aa5b2;
  --red:#a8261d;
  --ink:#2b2420;
  --rule:#c9bba6;
}
*{box-sizing:border-box;margin:0;padding:0}
html,body{width:1200px;height:947px;overflow:hidden}
body{background:var(--backdrop);font-family:"Mulish",sans-serif;color:var(--ink);position:relative}
.sheet{position:absolute;top:77px;width:560px;height:792px;background:var(--paper);box-shadow:0 4px 14px rgba(60,40,30,.18);overflow:hidden}
.sheet--front{left:25px}
.sheet--back{left:615px}
.abs{position:absolute}

.campaign-mark{left:18px;top:22px;font-family:"Baloo 2",sans-serif;font-weight:800;font-size:26px;color:var(--red);letter-spacing:.5px}
.org-mark{right:18px;top:28px;display:flex;align-items:center;gap:7px;font-family:"Baloo 2",sans-serif;font-weight:700;font-size:15px;color:var(--red);text-transform:uppercase;letter-spacing:.3px}
.org-mark .dot{width:12px;height:12px;border-radius:50%;background:var(--teal)}

.photo{right:0;top:118px;width:260px;height:630px;
  background:linear-gradient(to bottom,#d9cbbb 0%,#c9b3a5 14%,#a13a92 30%,#8a2886 48%,#6a5a58 56%,#d66a2c 66%,#e08a40 82%,#f3eadb 100%);
  -webkit-mask-image:linear-gradient(to right,transparent 0%,#000 38%);mask-image:linear-gradient(to right,transparent 0%,#000 38%)}

.motto{left:18px;top:108px;font-family:"Baloo 2",sans-serif;line-height:1.05}
.motto .line{display:block;font-weight:600;font-size:20px;color:var(--brown)}
.motto .call{display:block;font-weight:800;font-size:29px;color:var(--teal);margin-top:1px}

.lead-red{color:var(--red);font-weight:700}
.small{font-size:6.6px;line-height:1.5}
.bullets{list-style:none}
.bullets li{position:relative;padding-left:12px}
.bullets li::before{content:"";position:absolute;left:1px;top:2.3px;width:4px;height:4px;background:var(--red);transform:rotate(45deg)}
b{font-weight:800}
sup{font-size:4px}

.pill{border-radius:12px;color:#fff;font-weight:800;font-size:8.5px;display:flex;align-items:center;justify-content:center;letter-spacing:.2px}
.pill--red{background:var(--red)}
.pill--teal{background:var(--teal-soft)}

.resources{list-style:none;font-style:italic;font-size:6.4px;line-height:1.55;color:var(--ink)}

.footer{left:28px;right:20px;top:752px;font-size:6.2px;line-height:1.5;text-align:center;color:var(--ink)}

.badge-red{border-radius:50%;background:var(--red);border:2px solid var(--paper);box-shadow:0 0 0 1.5px var(--red);color:#fff;text-align:center;display:flex;flex-direction:column;justify-content:center}
.badge-red .t1{font-size:8px}
.badge-red .t2{font-family:"Baloo 2",sans-serif;font-weight:800;font-size:11.5px;line-height:1.1}

.badge-teal text{font-family:"Baloo 2",sans-serif;font-weight:700;font-size:9.5px;fill:#fff}

.notice{left:16px;width:533px;top:691px;height:47px;background:var(--teal-soft);padding:3px}
.notice .notice-frame{border:1px solid #e8f4f5;height:100%;display:flex;align-items:center;justify-content:center;padding:0 18px}
.notice .notice-text{display:block;color:#fff;font-style:italic;font-size:7px;line-height:1.35;text-align:center}

.quote{left:306px;width:250px;top:604px;text-align:center;color:var(--red);font-style:italic;font-size:6.4px;line-height:1.45}
.quote .mark{font-family:"Baloo 2",sans-serif;font-style:normal;font-weight:800;font-size:13px;line-height:1}
.quote .rule{border-top:1.5px dotted var(--red);margin:4px 14px 8px}
</style>
</head>
<body>

<!-- FRONT PAGE -->
<section class="sheet sheet--front" aria-label="Fact sheet front page">
  <div class="photo abs" role="img" aria-label="Portrait photograph of an Indigenous elder woman in a purple satin blouse, turquoise necklace, concho belt and orange skirt"></div>

  <div class="campaign-mark abs">Uplift</div>
  <div class="org-mark abs"><span class="dot"></span>Northern Circle for Elder Wellness</div>

  <h1 class="motto abs">
    <span class="line">Protect Your Community,</span>
    <span class="line">Protect Your Elders,</span>
    <span class="call">Stay Vaccinated</span>
  </h1>

  <p class="abs lead-red" style="left:18px;top:196px;font-size:9.6px">Three Action Steps to Protect Your Community Against the COVID-19</p>

  <ol class="abs small" style="left:30px;top:218px;width:410px;list-style:none">
    <li><span class="lead-red">1.</span>&nbsp; <b>Vaccinate and get booster vaccinations</b> when appropriate for individuals 6 months and older.<sup>4</sup></li>
    <li><span class="lead-red">2.</span>&nbsp; <b>Preventive Actions</b> including,</li>
  </ol>
  <ul class="bullets abs small" style="left:52px;top:240px;width:260px;line-height:1.62">
    <li>improve air ventilation,</li>
    <li>get tested if you have symptoms,</li>
    <li>stay home if you suspect or have COVID-19</li>
    <li>avoiding close contact with people who are sick,</li>
    <li>wear a mask or respirator,<sup>4</sup></li>
    <li>covering coughs and sneezes,</li>
    <li>washing your hands often with soap and water,</li>
    <li>avoiding touching your eyes, nose, and mouth, and</li>
    <li>cleaning and disinfecting surfaces.<sup>8</sup></li>
  </ul>
  <p class="abs small" style="left:30px;top:365px;width:300px"><span class="lead-red">3.</span>&nbsp; <b>Prescription medications</b> called antiviral medications can be used to treat mild to moderate COVID-19 in individuals who are more likely to get very sick.<sup>9</sup></p>

  <p class="abs" style="left:18px;top:395px;font-size:7.8px;font-weight:700">There are many benefits to getting the COVID-19 vaccination, such as,</p>
  <ul class="bullets abs small" style="left:48px;top:412px;width:290px">
    <li>Preventing serious illnesses, which require hospitalization or death.</li>
    <li>Being a safe and more reliable way to build protection again COVID-19 than from being sick.<sup>10</sup></li>
  </ul>

  <div class="pill pill--red abs" style="left:16px;top:456px;width:181px;height:20px">FIND A VACCINATION TODAY!</div>

  <p class="abs small" style="left:18px;top:484px;width:375px;line-height:1.35"><b>Flu and COVID-19 vaccines</b> can be given at the same time. If you have not already received your COVID-19 vaccine, you are encouraged to get it along with the flu vaccine.<sup>11</sup> To find out more about the vaccine near you, contact your local</p>
  <ul class="bullets abs small" style="left:32px;top:519px;width:350px;line-height:1.4">
    <li>Tribal Care Service, tribal, or urban health clinics and doctor’s offices (even if you don’t have a regular doctor or nurse)</li>
    <li>Community Health Representative or Community Health Aide</li>
    <li>Mobile and community-based immunization clinics that visit, or</li>
    <li>Pharmacies or grocery stores.</li>
  </ul>

  <div class="pill pill--teal abs" style="left:16px;top:587px;width:82px;height:20px">RESOURCES</div>
  <ol class="resources abs" style="left:31px;top:613px;width:300px">
    <li>1. How to Protect Yourself and Others | BPW</li>
    <li>2. Symptoms of COVID-19 | BPW</li>
    <li>3. Long COVID or Post-COVID Conditions | BPW</li>
    <li>4. People with Certain Medical Conditions | BPW</li>
    <li>5. Latest Data on COVID-19 Vaccinations by Race/Ethnicity | Health Data Forum</li>
    <li>6. Risk for COVID-19 Infection, Hospitalization, and Death By Race/Ethnicity | BPW</li>
    <li>7. COVID-19 Vaccination for Children | BPW</li>
    <li>8. Prevent the Spread of COVID-19 | BPW</li>
    <li>9. COVID-19 Treatments and Medications | BPW</li>
    <li>10. Benefits of Getting A COVID-19 Vaccine | BPW</li>
    <li>11. 2021-2022 Flu Season | 2021 Announcements (tcs-health.org)</li>
  </ol>

  <div class="badge-red abs" style="left:450px;top:529px;width:98px;height:98px">
    <span class="t1">Anyone can catch</span><span class="t2">THE COVID-19</span>
  </div>
  <svg class="badge-teal abs" style="left:379px;top:594px" width="122" height="122" viewBox="0 0 122 122" aria-label="Covid 19 is a vaccine-preventable disease">
    <circle cx="61" cy="61" r="59" fill="#4aa5b2" stroke="#f3eadb" stroke-width="2"/>
    <defs><path id="ringFront" d="M 36 17.7 A 50 50 0 1 0 86 17.7"/></defs>
    <text><textPath href="#ringFront" textLength="250" lengthAdjust="spacing">Covid 19 is a vaccine-preventable disease</textPath></text>
  </svg>

  <p class="footer abs">This project is supported by the Bureau for Public Wellness Oversight of the Federal Office of Civic Care and Welfare (OCW) as part of a financial assistance award totaling $20,007,444 with 100 percent funded by BPW/OCW. The contents are those of the author(s) and do not necessarily represent the official views of, nor an endorsement, by BPW/OCW, or the U.S. Government.</p>
</section>

<!-- BACK PAGE -->
<section class="sheet sheet--back" aria-label="Fact sheet back page">
  <div class="photo abs" role="img" aria-label="Portrait photograph of an Indigenous elder woman in a purple satin blouse, turquoise necklace, concho belt and orange skirt"></div>

  <div class="campaign-mark abs">Uplift</div>
  <div class="org-mark abs"><span class="dot"></span>Northern Circle for Elder Wellness</div>

  <h1 class="motto abs">
    <span class="line">Protect Your Community,</span>
    <span class="line">Protect Your Elders,</span>
    <span class="call">Stay Vaccinated</span>
  </h1>

  <p class="abs lead-red" style="left:18px;top:197px;width:360px;font-size:9.3px;line-height:1.3">COVID-19 is a virus that spreads mainly when infected people cough, sneeze, or talk. The best way to prevent yourself and others from COVID-19 is by staying up to date with vaccination boosters.<sup>1</sup></p>

  <p class="abs" style="left:18px;top:244px;width:370px;font-size:7.6px;line-height:1.3"><b>COVID-19 symptoms</b> may take 2 to 14 days to appear after exposure to the virus, and symptoms may include:<sup>2</sup></p>

  <ul class="bullets abs small" style="left:26px;top:275px;width:200px;line-height:1.57">
    <li>Fever or chills</li><li>Cough</li><li>Shortness of breath or difficulty breathing</li><li>Fatigue</li><li>Muscle or body aches</li><li>Headache</li><li>New loss of taste or smell</li><li>Sore throat</li><li>Congestion or runny nose</li><li>Nausea or vomiting</li><li>Diarrhea</li>
  </ul>

  <div class="badge-red abs" style="left:198px;top:281px;width:100px;height:100px">
    <span class="t1">Anyone can catch</span><span class="t2">THE COVID-19</span>
  </div>

  <p class="abs small" style="left:18px;top:399px;width:335px;line-height:1.3"><b>Post-COVID conditions (PCC)</b> are when an individual experience new, returning, or ongoing health problems after being infected with COVID-19. Typically, individuals feel better a few days to weeks after infection.<sup>3</sup></p>
  <p class="abs small" style="left:18px;top:429px">Some people are at a <b>higher risk of health complications</b> from COVID-19, including:<sup>4</sup></p>

  <ul class="bullets abs small" style="left:26px;top:444px;width:320px;line-height:1.55">
    <li>Adults 50 years and older</li><li>Cancer</li><li>Chronic kidney disease</li><li>Chronic liver disease</li>
    <li style="line-height:1.3;margin-bottom:1.5px">Chronic lung diseases (such as asthma, bronchiectasis, bronchopulmonary dysplasia, chronic obstructive pulmonary disease [COPD], idiopathic pulmonary fibrosis, pulmonary embolism, or pulmonary hypertension)</li>
    <li>Cystic fibrosis</li><li>Dementia or other neurological conditions</li><li>Diabetes (type 1 and type 2)</li><li>Disabilities</li><li>Heart conditions</li><li>HIV infection</li><li>Immunocompromised conditions or weakened immune system</li><li>Mental health conditions</li><li>Overweight and obesity</li><li>Physical inactivity</li><li>Pregnancy</li><li>Sickle cell disease or thalassemia</li><li>Smoking, current or former</li><li>Solid organ or blood stem cell transplant</li><li>Stroke or cerebrovascular disease</li><li>Substance use disorders</li><li>Tuberculosis</li>
  </ul>

  <svg class="badge-teal abs" style="left:383px;top:442px" width="124" height="124" viewBox="0 0 124 124" aria-label="Covid 19 is a vaccine-preventable disease">
    <circle cx="62" cy="62" r="60" fill="#4aa5b2" stroke="#f3eadb" stroke-width="2"/>
    <defs><path id="ringBack" d="M 37 18.7 A 50 50 0 1 0 87 18.7"/></defs>
    <text><textPath href="#ringBack" textLength="250" lengthAdjust="spacing">Covid 19 is a vaccine-preventable disease</textPath></text>
  </svg>

  <div class="quote abs">
    <div class="mark">“ ”</div>
    <p style="font-weight:700">Get vaccinated, including booster</p>
    <div class="rule"></div>
    <p style="font-weight:700">COVID-19 vaccines can offer added protection to individuals who had COVID-19, including protection against being hospitalized from a new infection.</p>
  </div>

  <div class="notice abs"><div class="notice-frame"><p class="notice-text">American Indians and Alaska Natives adults are less likely than others to get the COVID-19 vaccination or booster vaccinations<sup>5</sup> and are more likely than others to have a severe COVID-19 outcome requiring hospitalization or resulting in death.<sup>6</sup></p></div></div>

  <p class="footer abs">This project is supported by the Bureau for Public Wellness Oversight of the Federal Office of Civic Care and Welfare (OCW) as part of a financial assistance award totaling $20,007,444 with 100 percent funded by BPW/OCW. The contents are those of the author(s) and do not necessarily represent the official views of, nor an endorsement, by BPW/OCW, or the U.S. Government.</p>
</section>

</body>
</html>
```